Medical supplies company needs a catalogue re-design

Our present catalogue is spread over a number of pages but this needs to be reduced. 4-5 images would require to be on each page. It needs to be professional, simple and elegant. The photos and descriptors need to be adjacent to each other. It should be able to be emailed conventionally as an e-catalogue without it being compressed. an email with existing catalogue will be emailed to anyone interested.
https://www.quillvault.net/s/81tazup7rqwmdlon/consumables%20photos%20and%20descriptions.pdf?dl=0
Target Market(s)
medical practices, hospitals
Industry/Entity Type
Medical Supply

```html
<!DOCTYPE html>
<html lang="en">
<head>
<meta charset="utf-8">
<title>Medical Supplies Catalogue</title>
<link href="https://fonts.googleapis.com/css2?family=Fira+Sans:wght@300;400;500;600&display=swap" rel="stylesheet">
<style>
:root{
  --backdrop:#cbcbcb;
  --page:#ffffff;
  --column:#f1f2f4;
  --navy:#1b3556;
  --title:#1c3a5e;
  --rule:#86a8d2;
  --accent:#5b8fd0;
  --body:#2e3e52;
}
*{margin:0;padding:0;box-sizing:border-box}
html,body{width:1200px;height:1122px;overflow:hidden;background:var(--backdrop)}
body{font-family:"Fira Sans",sans-serif;color:var(--body);position:relative}
.page{position:absolute;top:290px;width:382px;height:543px;background:var(--page);overflow:hidden}
.page--gloves{left:13px}
.page--sutures{left:409px}
.page--daily{left:805px}
.column{position:absolute;left:27px;width:120px;background:var(--column)}
.section-title{position:absolute;left:18px;font-weight:500;font-size:23.5px;color:var(--navy);letter-spacing:.2px;line-height:1;white-space:nowrap}
.section-rule{position:absolute;left:18px;right:18px;height:1.5px;background:var(--rule)}
.divider{position:absolute;left:18px;right:18px;height:1px;background:#b9cbe3}
.photo{position:absolute;left:36px;width:102px}
.entry{position:absolute;left:157px;width:212px}
.entry h3{font-weight:600;font-size:11.4px;line-height:14px;color:var(--title);white-space:nowrap}
.entry h3.entry-title--long{font-size:10px;line-height:12px}
.entry h4{font-weight:600;font-size:8.6px;color:var(--title);margin-top:1px}
.entry h5{font-weight:600;font-size:8.6px;color:var(--accent);margin-top:4px}
.entry ul{list-style:none;margin-top:3px}
.entry li,.entry p{font-weight:300;font-size:7.4px;line-height:9px;margin-bottom:5.8px}
.entry li{padding-left:5px;text-indent:-5px}
.entry li::before{content:"• "}
.grid{display:grid;grid-template-columns:repeat(3,73px)}
.grid--two{grid-template-columns:repeat(2,110px)}
</style>
</head>
<body>

<section class="page page--gloves">
  <h2 class="section-title" style="top:24px">Gloves</h2>
  <div class="section-rule" style="top:48px"></div>
  <div class="column" style="top:49px;height:494px"></div>

  <div class="photo" role="img" aria-label="Box of nitrile powder free gloves" style="top:67px;height:78px;background:linear-gradient(135deg,#f4f4f4,#d8d8da)"></div>
  <div class="entry" style="top:71px">
    <h3>Nitrile Powder Free<br>and Latex Free Gloves</h3>
    <ul>
      <li>Provides great tactile sensitivity because of normal fingertip thickness</li>
      <li>Powder free</li>
      <li>Latex free</li>
      <li>Ambidextrous</li>
    </ul>
    <p>Small, Medium, Large (box of 100)</p>
  </div>
  <div class="divider" style="top:195px"></div>

  <div class="photo" role="img" aria-label="Box of latex examination gloves" style="top:214px;height:102px;background:linear-gradient(135deg,#f6f6f6,#d6d6d8)"></div>
  <div class="entry" style="top:219px">
    <h3>Latex Examination Gloves<br>(non sterile, powder free)</h3>
    <ul>
      <li>Ambidextrous</li>
      <li>Powder free</li>
      <li>Natural Latex with beaded cuff</li>
      <li>Good Grip</li>
    </ul>
    <p>Small, Medium, Large (100 gloves per box)</p>
  </div>
  <div class="divider" style="top:334px"></div>

  <div class="photo" role="img" aria-label="Box of latex surgical gloves" style="top:343px;height:76px;background:linear-gradient(135deg,#eef0f6,#c9cfe0)"></div>
  <div class="entry" style="top:347px">
    <h3>Latex Surgical Gloves</h3>
    <h4>Two types: With and without powder</h4>
    <h5>Without powder:</h5>
    <ul>
      <li>Powder free</li>
      <li>Non irritating</li>
      <li>Textured</li>
      <li>Sterile</li>
      <li>6.5, 7, 7.5, 8 (boxes of 50 pairs)</li>
    </ul>
    <h5>Sterile Latex Gloves with powder:</h5>
    <ul>
      <li>Good grip and feel</li>
      <li>Natural anatomical design reduces thumb and arm stress and results in greater comfort</li>
      <li>7, 7.5, 8 (box of 50 pairs)</li>
    </ul>
  </div>
</section>

<section class="page page--sutures">
  <h2 class="section-title" style="top:24px">Sutures</h2>
  <div class="section-rule" style="top:48px"></div>
  <div class="column" style="top:49px;height:228px"></div>

  <div class="photo" role="img" aria-label="Box of nylon monofilament sutures" style="top:67px;height:96px;background:linear-gradient(160deg,#dff0f7,#5fb8df 60%,#9fdc9a)"></div>
  <div class="entry" style="top:71px">
    <h3 class="entry-title--long">Nylon Monofilament Polyamide<br>Suture With Needle and Latex Free Gloves</h3>
    <ul>
      <li>2 types: Standard and Deluxe</li>
      <li>Different size needles according to suture material.</li>
      <li>Smooth and easy to tie knots</li>
      <li>12 per box (3/0, 4/0, 5/0)</li>
    </ul>
  </div>
  <div class="divider" style="top:172px"></div>

  <div class="photo" role="img" aria-label="Boxes of braided silk sutures" style="top:182px;height:85px;background:linear-gradient(135deg,#f2f6f9,#8fcbe8)"></div>
  <div class="entry" style="top:187px">
    <h3>Silk Suture Braided With Needle</h3>
    <ul>
      <li>Non absorbable, braided and coated sutures made of natural silk filaments</li>
      <li>Excellent handling and knot security</li>
      <li>12 per box</li>
      <li>3/0, 4/0 and 5/0</li>
    </ul>
  </div>
  <div class="divider" style="top:277px"></div>

  <h2 class="section-title" style="top:286px">Needles and Syringes</h2>
  <div class="section-rule" style="top:315px"></div>
  <div class="column" style="top:316px;height:227px"></div>

  <div class="photo" role="img" aria-label="Box of sterile hypodermic needles" style="top:334px;height:78px;background:linear-gradient(135deg,#e8f3ea,#f4f4f6 55%,#f1c9d6)"></div>
  <div class="entry" style="top:339px">
    <h3 class="entry-title--long">Premium Grade Sterile Hypodermic Needles</h3>
    <p style="margin-top:3px;margin-bottom:4px">Regular bevel and wall type, Box of 100</p>
    <ul class="grid">
      <li>18g 38mm</li><li>21g 25mm</li><li>25g 25mm</li>
      <li>19g 38mm</li><li>23g 32mm</li><li>25g 16mm</li>
      <li>21g 38mm</li><li>23g 19mm</li>
    </ul>
  </div>
  <div class="divider" style="top:420px"></div>

  <div class="photo" role="img" aria-label="Box of 5ml syringes" style="top:430px;height:77px;background:linear-gradient(135deg,#eef3fb,#c6d6ee)"></div>
  <div class="entry" style="top:435px">
    <h3>Syringes</h3>
    <p style="margin-top:3px;margin-bottom:4px">Sterile, single use Integrated Veloria Luer slip type Clear polycarbonate barrel</p>
    <ul class="grid grid--two">
      <li>1ml (box of 100)</li><li>10ml (box of 100)</li>
      <li>3ml (box of 100)</li><li>20ml (box of 100)</li>
      <li>5ml (box of 100)</li><li>50ml (box of 20)</li>
    </ul>
  </div>
</section>

<section class="page page--daily">
  <h2 class="section-title" style="top:24px">Consumer Health and Daily Aids</h2>
  <div class="section-rule" style="top:48px"></div>
  <div class="column" style="top:49px;height:494px"></div>

  <div class="photo" role="img" aria-label="Automatic blood pressure monitor with cuff" style="top:67px;height:74px;background:linear-gradient(135deg,#f2f4fa,#7fa0d8)"></div>
  <div class="entry" style="top:72px">
    <h3>Blood Pressure Monitor</h3>
    <ul>
      <li>Accurate and reliable</li>
      <li>Automatic measurement of systolic, diastolic and pulse</li>
      <li>80 memories and average test results</li>
      <li>Indication of blood pressure standard</li>
      <li>Efficacious and low noise pump</li>
      <li>Big screen and easy to read</li>
      <li>Automatic power off</li>
      <li>MDRA Approved</li>
    </ul>
  </div>
  <div class="divider" style="top:215px"></div>

  <div class="photo" role="img" aria-label="Folded nonwoven disposable bed sheet" style="top:234px;height:83px;background:linear-gradient(135deg,#d4d4d6,#aeb0b4)"></div>
  <div class="entry" style="top:245px">
    <h3>Nonwoven Disposable Bed Sheets</h3>
    <ul>
      <li>Nonwoven Disposable Bed Sheets 100 x 200cm</li>
      <li>Navy Blue 40GSM thickness</li>
      <li>Exceptional Quality</li>
      <li>Can be bought in lots of 10</li>
    </ul>
  </div>
  <div class="divider" style="top:335px"></div>

  <div class="photo" role="img" aria-label="Absorbent underpad" style="top:354px;height:68px;background:radial-gradient(circle,#f7f7f7 50%,#9fd0ea)"></div>
  <div class="entry" style="top:358px">
    <h3>Absorbent Underpad</h3>
    <ul>
      <li>Heavy Duty 40g, Sap 2g, blue, 40x60cm</li>
      <li>Provides surface protection for beds, mattresses and wheelchairs.</li>
      <li>Super absorbent and provides extra dryness and comfort.</li>
      <li>Pack of 150</li>
    </ul>
  </div>
</section>

</body>
</html>
```